Real Estate Business Folders, Business Cards, Envelopes & Letterhead

Im looking for trendy, modern & professional design concepts for my business folder that will be used for real estate documents and property report presentations. I'm also looking for Business card designs, envelopes and letterhead with a similar theme. I have a logo already and I would like the logo colors to be incorporated in the design concepts.

Target Market(s)

Real Estate Investors, Banks, Financial Institutions

Industry/Entity Type

Real Estate

Colors
0455a3
959595
d3d3d3
848484

Requirements
Must have
• Trendy Modern, High Class look. Please include logo and colors and incorporate some silver or metallic.
• Business Address: 4812 Corvelle Blvd ste 210-300
• Cedar Basin, NV 89550
• Phone: 702-555-0147
• Fax : 702-555-0183
• Email: info@mesacrestlandgroup.example
• Website: MesaCrestLandGroup.example

```html
<!DOCTYPE html>
<html lang="en">
<head>
<meta charset="utf-8">
<title>Mesa Crest Land Group – Stationery Set</title>
<link rel="stylesheet" href="https://fonts.googleapis.com/css2?family=Tinos&family=Roboto:wght@400;700&family=Roboto+Condensed:wght@700&display=swap">
<style>
:root{
  --brand-blue:#0455a3;
  --brand-blue-light:#3f86d6;
  --silver:#959595;
  --silver-light:#d3d3d3;
  --grey:#848484;
  --paper:#ffffff;
  --ink:#6e6e6e;
  --backdrop:#8fb8e3;
}
*{box-sizing:border-box;margin:0;padding:0}
html,body{width:1200px;height:904px;overflow:hidden;background:var(--backdrop)}
body{position:relative;font-family:'Roboto',Arial,sans-serif}
.piece{position:absolute;background:var(--paper);box-shadow:0 4px 10px rgba(0,40,90,.25);overflow:hidden}

.brand{display:flex;align-items:center;gap:6px}
.brand-mark{width:12px;height:12px;background:var(--brand-blue);flex:none}
.brand-name{font-family:'Tinos',serif;font-weight:400;color:var(--brand-blue);white-space:nowrap;line-height:1}
.tagline{font-family:'Tinos',serif;color:var(--grey);letter-spacing:.18em;white-space:nowrap}

/* letterhead */
.letterhead{left:100px;top:27px;width:344px;height:492px}
.letterhead .edge{position:absolute;left:20px;top:72px;width:8px;height:410px;background:linear-gradient(90deg,var(--silver-light),var(--silver))}
.letterhead .tab{position:absolute;left:20px;top:2px;width:8px;height:22px;background:var(--brand-blue)}
.letterhead .brand{position:absolute;left:20px;top:50px}
.letterhead .brand-name{font-size:17px}
.letterhead .tagline{position:absolute;left:20px;top:71px;font-size:5px}
.letterhead .contact{position:absolute;left:245px;top:28px;font-size:4.6px;line-height:7.6px;color:var(--brand-blue);font-style:normal}
.letterhead .body{position:absolute;left:49px;top:100px;width:270px;font-size:6.2px;line-height:10.8px;color:var(--ink)}
.letterhead .body p{margin-bottom:10px}
.letterhead .faint{position:absolute;left:32px;bottom:8px;opacity:.12}

/* folder */
.folder{left:437px;top:70px;width:344px;height:493px}
.folder .offer{position:absolute;left:8px;top:190px;width:140px;padding:6px 12px;background:rgba(255,255,255,.18);font-family:'Roboto Condensed',sans-serif;font-weight:700;font-size:13px;line-height:18.5px;color:#fff}
.folder .offer li{list-style:none;display:flex;align-items:center;gap:6px}
.folder .offer li::before{content:"";width:7px;height:7px;border-radius:50%;background:var(--silver-light)}
.folder .brand{position:absolute;left:150px;top:410px}
.folder .brand-name{font-size:21px}
.folder .tagline{position:absolute;left:150px;top:436px;font-size:7px}

/* business cards */
.card{width:155px;height:90px}
.card-front{left:830px;top:85px;background:var(--brand-blue)}
.card-front .brand{position:absolute;left:28px;top:30px}
.card-front .brand-mark{background:#fff}
.card-front .brand-name{color:#fff;font-size:12px}
.card-front .strip{position:absolute;left:0;bottom:0;width:100%;height:20px;background:var(--paper);clip-path:polygon(0 40%,100% 0,100% 100%,0 100%)}
.card-front .web{position:absolute;right:14px;bottom:5px;font-size:4.5px;color:var(--brand-blue);font-weight:700}
.card-back{left:830px;top:205px}
.card-back .panel{position:absolute;right:0;top:0;width:78px;height:100%;background:var(--brand-blue);clip-path:polygon(22% 0,100% 0,100% 100%,0 100%)}
.card-back .brand{position:absolute;right:8px;top:30px}
.card-back .brand-mark{background:#fff;width:7px;height:7px}
.card-back .brand-name{color:#fff;font-size:7px}
.card-back .who{position:absolute;left:8px;top:14px;font-size:5px;color:var(--brand-blue);font-weight:700}
.card-back .who span{display:block;font-weight:400;color:var(--grey)}
.card-back .lines{position:absolute;left:8px;top:34px;font-size:4.2px;line-height:7px;color:var(--grey)}
.card-back .addr{position:absolute;left:0;bottom:6px;width:90px;padding:3px 8px;background:var(--brand-blue);font-size:4px;line-height:5.5px;color:#fff}

/* notebook */
.notebook{left:830px;top:330px;width:145px;height:230px;border-radius:0 10px 10px 0;background:linear-gradient(180deg,var(--brand-blue-light),var(--brand-blue))}
.notebook .band{position:absolute;left:105px;top:0;width:7px;height:100%;background:#444}
.notebook .brand{position:absolute;left:22px;top:95px}
.notebook .brand-mark{background:#fff}
.notebook .brand-name{color:#fff;font-size:14px}
.notebook .web{position:absolute;right:8px;bottom:12px;font-size:4.5px;color:#fff}

/* thank-you card */
.thanks{left:95px;top:590px;width:340px;height:260px}
.thanks .script{position:absolute;right:0;top:0;width:150px;height:246px;background:var(--brand-blue);border-radius:140px 0 0 0}
.thanks .brand{position:absolute;left:20px;top:196px}
.thanks .brand-name{font-size:17px}
.thanks .tagline{position:absolute;left:20px;top:218px;font-size:6px}
.thanks .footer{position:absolute;left:0;bottom:0;width:100%;height:14px;background:var(--brand-blue);font-size:5px;line-height:14px;color:#fff;padding-left:20px;white-space:nowrap}

/* envelope */
.envelope{left:700px;top:600px;width:390px;height:250px}
.envelope .brand{position:absolute;left:16px;top:22px}
.envelope .brand-name{font-size:16px}
.envelope .tagline{position:absolute;left:16px;top:42px;font-size:5px}
.envelope .return{position:absolute;left:16px;top:52px;font-size:4.5px;color:var(--brand-blue);font-weight:700}
.envelope .faint{position:absolute;left:130px;bottom:14px;opacity:.12}
.envelope .rule{position:absolute;left:0;bottom:0;width:100%;height:6px;background:linear-gradient(90deg,var(--silver-light),var(--brand-blue) 60%,var(--silver-light))}
</style>
</head>
<body>

<section class="piece letterhead">
  <div class="tab"></div>
  <div class="edge"></div>
  <div class="brand"><span class="brand-mark"></span><span class="brand-name">MESA CREST</span></div>
  <div class="tagline">LAND GROUP</div>
  <address class="contact">
    4812 Corvelle Blvd ste 210-300<br>Cedar Basin, NV 89550<br>
    702-555-0147 · 702-555-0183<br>info@mesacrestlandgroup.example<br>MesaCrestLandGroup.example
  </address>
  <div class="body">
    <p>Lorem Ipsum is simply dummy text of the printing and typesetting industry. Lorem Ipsum has been the industry's standard dummy text ever since the 1500s, when an unknown printer took a galley of type and scrambled it to make a type specimen book. It has survived not only five centuries, but also the leap into electronic typesetting, remaining essentially unchanged.</p>
    <p>It is a long established fact that a reader will be distracted by the readable content of a page when looking at its layout. The point of using Lorem Ipsum is that it has a more-or-less normal distribution of letters, as opposed to using content here, content here, making it look like readable English.</p>
    <p>Contrary to popular belief, Lorem Ipsum is not simply random text. It has roots in a piece of classical Latin literature from 45 BC, making it over 2000 years old. The generated Lorem Ipsum is therefore always free from repetition, injected humour, or non-characteristic words etc.</p>
  </div>
  <svg class="faint" width="300" height="110" viewBox="0 0 300 110"><rect x="0" y="30" width="70" height="80" fill="#555"/><rect x="80" y="50" width="200" height="60" fill="#555"/></svg>
</section>

<section class="piece folder">
  <svg width="344" height="493" viewBox="0 0 344 493">
    <defs><linearGradient id="cityGlow" x1="0" y1="0" x2="1" y2="1"><stop offset="0" stop-color="#6a8fc9"/><stop offset=".5" stop-color="#b0726a"/><stop offset="1" stop-color="#3a3f6a"/></linearGradient></defs>
    <rect width="344" height="493" fill="url(#cityGlow)" role="img" aria-label="Night photograph of a city skyline with lit towers"/>
    <rect width="344" height="6" fill="#f2c98a"/>
    <polygon points="0,430 344,222 344,242 30,440 0,470" fill="var(--brand-blue)"/>
    <polygon points="80,420 344,262 344,493 180,493" fill="#fff"/>
    <polygon points="0,470 30,440 180,493 0,493" fill="var(--brand-blue)"/>
    <polygon points="220,0 344,0 344,110" fill="var(--brand-blue)" opacity=".55"/>
  </svg>
  <ul class="offer"><li>NO HASSLES</li><li>NO FEES</li><li>NO REPAIRS</li><li>NO HEADACHES!!</li></ul>
  <div class="brand"><span class="brand-mark"></span><span class="brand-name">MESA CREST</span></div>
  <div class="tagline">LAND GROUP</div>
</section>

<section class="piece card card-front">
  <div class="brand"><span class="brand-mark"></span><span class="brand-name">MESA CREST</span></div>
  <div class="strip"></div>
  <div class="web">MesaCrestLandGroup.example</div>
</section>

<section class="piece card card-back">
  <div class="panel"></div>
  <div class="brand"><span class="brand-mark"></span><span class="brand-name">MESA CREST</span></div>
  <div class="who">Example Name<span>Position</span></div>
  <div class="lines">702-555-0147<br>702-555-0183<br>info@mesacrestlandgroup.example<br>MesaCrestLandGroup.example</div>
  <div class="addr">4812 Corvelle Blvd ste 210-300<br>Cedar Basin, NV 89550</div>
</section>

<section class="piece notebook">
  <div class="band"></div>
  <div class="brand"><span class="brand-mark"></span><span class="brand-name">MESA CREST</span></div>
  <div class="web">MesaCrestLandGroup.example</div>
</section>

<section class="piece thanks">
  <div class="script" role="img" aria-label="Hand-lettered thank you script in white"></div>
  <div class="brand"><span class="brand-mark"></span><span class="brand-name">MESA CREST</span></div>
  <div class="tagline">LAND GROUP</div>
  <div class="footer">4812 Corvelle Blvd ste 210-300 Cedar Basin, NV 89550 · 702-555-0147 · info@mesacrestlandgroup.example</div>
</section>

<section class="piece envelope">
  <div class="brand"><span class="brand-mark"></span><span class="brand-name">MESA CREST</span></div>
  <div class="tagline">LAND GROUP</div>
  <div class="return">4812 Corvelle Blvd ste 210-300 Cedar Basin, NV 89550</div>
  <svg class="faint" width="240" height="90" viewBox="0 0 240 90"><rect x="0" y="10" width="60" height="80" fill="#555"/><rect x="70" y="40" width="160" height="50" fill="#555"/></svg>
  <div class="rule"></div>
</section>

</body>
</html>
```